Voranel.com Personal Trainer/Fitness Website

I want a website to market my personal training/Outdoor Bootcamp Class services, as well as to ditribute nutrivexa. I need a logo as well I included an address for the Harbor Gales 1975 logo. I'd like Voranel in place of Harbor Gales, and in Black and white, just different enough so I can't get sued by the PLX.
https://www.pictofind.example/imgres?imgurl=http%3A%2F%2Fwww.dorian-halverstock.example%2Fwp-content%2Fuploads%2F2014%2F01%2Fgales_mark4.jpg&imgrefurl=http%3A%2F%2Fwww.dorian-halverstock.example%2Fplx-emblem-reworks-tulsa-harbor-bolts%2F&docid=_qweRT8uPLmnBx&tbnid=k3tyA7XbNqwePZ%3A&w=600&h=450&client=ms-android-carrierx&bih=512&biw=360&ved=0ahUKEwiQazxcv7LMAhUTwGMKHRPMBWMQMwg6KBQwFA&iact=mrc&uact=8.
It should be about 5 pages 1. home 2. about 3. Services 4. Blog/Videos and programs 5. Contact.
http://www.tobenwelfitness.example.uk/ is a website I like the style of.

Target Market(s)

Seattle area

Industry/Entity Type

Fitness

Coding

Coded - Design and coding required

Number of Pages Required

4 page

Font styles to use
Serif
Sans Serif

Requirements
Must have
• A minimal look
Nice to have
• A logo similar to the 1975 Harbor Galewinds Logo, with a Small Dorn Velask ripping his shirt open(with a picture of the logo on his shirt, picture within picture) to turn into Skyvaler in the center. Skyline is black, Background and small figure white(with black logo on shirt)

```html
<!DOCTYPE html>
<html lang="en">
<head>
<meta charset="utf-8">
<title>Voranel – Personal Trainer Mayfair</title>
<link rel="stylesheet" href="https://fonts.googleapis.com/css2?family=Varela+Round&family=Ubuntu:wght@400;500&family=Tinos&display=swap">
<style>
  :root{
    --ink:#231f20;
    --paper:#ffffff;
    --stage:#ececec;
    --muted:#d9d9d9;
    --hero-a:#3a3634;
    --hero-b:#8a6450;
    --hero-c:#4d4a4c;
    --photo-a:#c9d4dc;
    --photo-b:#6d5a4c;
  }
  *{box-sizing:border-box;margin:0;padding:0}
  html,body{width:1200px;height:1200px;overflow:hidden;background:var(--stage)}
  body{position:relative;font-family:"Varela Round",sans-serif;color:var(--ink)}
  .page{position:absolute;left:125px;top:4px;width:950px;height:1192px;background:var(--paper);box-shadow:0 6px 24px rgba(0,0,0,.25);overflow:hidden}
  .abs{position:absolute}

  .topbar{left:0;top:0;width:950px;height:42px;background:var(--ink);color:var(--paper);font-size:12px}
  .topbar .call{left:36px;top:15px}
  .topbar .social{left:702px;top:13px;display:flex;gap:12px}
  .topbar .social span{display:block;width:16px;height:16px;border:1.5px solid var(--paper);border-radius:3px}
  .topbar .mail{left:760px;top:14px}
  .topbar .search{left:849px;top:15px}
  .topbar .lens{left:902px;top:11px}

  .header{left:0;top:42px;width:950px;height:128px}
  .brand{left:70px;top:44px;display:flex;align-items:center;gap:8px;font-size:18px;letter-spacing:1px}
  .brand i{display:block;width:22px;height:22px;border-radius:50%;background:var(--ink)}
  .nav{left:596px;top:62px;display:flex;gap:14px;font-size:12px;letter-spacing:.2px}

  .hero{left:0;top:170px;width:950px;height:317px;background:linear-gradient(100deg,var(--hero-a) 0%,var(--hero-b) 38%,var(--hero-c) 62%,var(--hero-b) 78%,var(--hero-a) 100%)}
  .hero .shade{inset:0;background:rgba(30,26,26,.35)}
  .hero .kicker{left:0;width:950px;top:108px;text-align:center;color:var(--paper);font-size:14.5px}
  .hero h1{left:0;width:950px;top:146px;text-align:center;color:var(--paper);font-family:"Ubuntu",sans-serif;font-weight:500;font-size:30px;letter-spacing:.5px}
  .hero .cta{left:385px;top:202px;width:182px;height:46px;border:2px solid var(--paper);color:var(--paper);font-family:"Ubuntu",sans-serif;font-size:21px;display:flex;align-items:center;justify-content:center}

  .portrait{left:43px;top:560px;width:234px;height:234px;border-radius:50%;background:radial-gradient(circle at 55% 40%,var(--photo-b) 0%,#4a3b32 45%,var(--photo-a) 75%)}
  .intro{left:310px;top:545px;width:580px}
  .intro h2{font-weight:400;font-size:22px;margin-bottom:12px}
  .intro p{font-size:13.3px;line-height:17px;margin-bottom:17px}

  .service{top:874px;width:260px;text-align:center}
  .service .icon{display:block;margin:0 auto 8px}
  .service h3{font-weight:400;font-size:14px;margin-bottom:6px}
  .service p{font-family:"Tinos",serif;font-size:11px;line-height:14.5px}

  .footer{left:0;top:1083px;width:950px;height:109px;background:var(--ink);color:var(--paper)}
  .fcol{top:15px}
  .fcol h4{font-weight:400;font-size:13.5px;margin-bottom:4px}
  .fcol p{font-size:11.3px;line-height:18px}
  .fcol.tight p{line-height:14.5px}
</style>
</head>
<body>
<div class="page">

  <div class="abs topbar">
    <div class="abs call">Call Today: 0000 000 000</div>
    <div class="abs social" aria-label="Social links"><span></span><span></span></div>
    <svg class="abs mail" width="18" height="14" viewBox="0 0 18 14" fill="none" stroke="#fff" stroke-width="1.4" aria-label="Email"><rect x="1" y="1" width="16" height="12" rx="1"/><path d="M1 1l8 7 8-7"/></svg>
    <div class="abs search">Search</div>
    <svg class="abs lens" width="20" height="20" viewBox="0 0 20 20" fill="none" stroke="#fff" stroke-width="1.8" aria-label="Search"><circle cx="12" cy="8" r="6"/><path d="M7.5 12.5L2 18"/></svg>
  </div>

  <div class="abs header">
    <div class="abs brand"><i></i>VORANEL</div>
    <nav class="abs nav"><span>HOME</span><span>ABOUT</span><span>SERVICES</span><span>BLOG</span><span>CONTACT</span></nav>
  </div>

  <section class="abs hero" role="img" aria-label="Photo of a woman and a man training with dumbbells in a gym">
    <div class="abs shade"></div>
    <p class="abs kicker">Premium personal training services in the Mayfair area</p>
    <h1 class="abs">PERSONAL TRAINER MAYFAIR</h1>
    <div class="abs cta">GET IN TOUCH</div>
  </section>

  <div class="abs portrait" role="img" aria-label="Portrait photo of the personal trainer in a gym"></div>
  <section class="abs intro">
    <h2>Personal Training in Voranel</h2>
    <p>I work exclusively with men and women who are trying to make a difference in their personal lives. Working long hours can make it hard to find time to build your stamina, shred muscle and lose some weight.</p>
    <p>My personal training studio in Mayfair is conveniently located under Halvora hotel. This is not another noisy gym that will let you down by forcing you to try and figure it out on your own. Let me guide you with my knowledge, and keep you engaged with fun workouts that will get you in the best shape of your life.</p>
    <p>You have everything to gain from incorporating a holistic approach to health and fitness. My personality and style of training are infectious, and my forward vision is to “infect” you into a healthy way of thinking and way of life. Holiday season is never too far away. How do you want to look on the beach this year?</p>
  </section>

  <div class="abs service" style="left:74px">
    <svg class="icon" width="70" height="70" viewBox="0 0 70 70" aria-label="Dumbbell icon"><circle cx="35" cy="35" r="35" fill="#231f20"/><g fill="none" stroke="#fff" stroke-width="2.5" stroke-linecap="round"><path d="M12 30v10M17 24v22M22 24v22M48 24v22M53 24v22M58 30v10M22 35h26"/></g></svg>
    <h3>Personal Training</h3>
    <p>Private Personal Training<br>100% Customized Exercise Programming<br>Customized Nutrition and Supplementation</p>
  </div>
  <div class="abs service" style="left:345px">
    <svg class="icon" width="70" height="70" viewBox="0 0 70 70" aria-label="Laptop icon"><circle cx="35" cy="35" r="35" fill="#231f20"/><g fill="none" stroke="#fff" stroke-width="2.5"><rect x="19" y="21" width="32" height="22" rx="1.5"/><path d="M14 48h42"/></g></svg>
    <h3>Online Coaching</h3>
    <p>Personal Training From A Distance<br>24 Hour Support and Contact<br>Customized Nutrition and Supplementation</p>
  </div>
  <div class="abs service" style="left:616px">
    <svg class="icon" width="70" height="70" viewBox="0 0 70 70" aria-label="Group icon"><circle cx="35" cy="35" r="35" fill="#231f20"/><g fill="#fff"><circle cx="22" cy="30" r="5"/><circle cx="48" cy="30" r="5"/><path d="M13 47c0-7 4-11 9-11s9 4 9 11z"/><path d="M39 47c0-7 4-11 9-11s9 4 9 11z"/><circle cx="35" cy="27" r="6"/><path d="M24 49c0-8 5-13 11-13s11 5 11 13z"/></g></svg>
    <h3>Small Group</h3>
    <p>Work with 2-3 of Your Friends<br>Boot Camp Style Personal Training<br>Customized Nutrition and Supplementation</p>
  </div>

  <footer class="abs footer">
    <div class="abs fcol" style="left:269px">
      <h4>Nagivation</h4>
      <p>Home<br>Services<br>Blog<br>Contact</p>
    </div>
    <div class="abs fcol" style="left:443px">
      <h4>Contact</h4>
      <p>Phone: 00000 000 000<br>Email: contact@voranel.example</p>
    </div>
    <div class="abs fcol tight" style="left:617px">
      <h4>Location</h4>
      <p>Halvora<br>48 Carrow Lane<br>London<br>W1K 7QR</p>
    </div>
  </footer>

</div>
</body>
</html>
```